Quill Ridge Business cards

We need business cards for our aviation company called Quill Ridge Aviation. The colour scheme is the same as the one in the logo you design (metallic green/ similar to the colours on the aircraft). The design needs to be unique and stand out.

Industry/Entity Type

Business

```html
<!DOCTYPE html>
<html lang="en">
<head>
<meta charset="utf-8">
<title>Quill Ridge Aviation — Business Cards</title>
<link rel="stylesheet" href="https://fonts.googleapis.com/css2?family=Arimo:wght@400;700&display=swap">
<style>
  :root {
    --canvas: #ecebe6;
    --card: #ffffff;
    --green: #3a9a48;
    --green-dark: #1f5a2a;
    --olive: #b8bc1e;
    --olive-light: #d6d63a;
    --brown: #9c6a2c;
    --gold: #b8891f;
    --ink: #1f4a22;
  }
  * { margin: 0; padding: 0; box-sizing: border-box; }
  html, body { width: 1200px; height: 1200px; overflow: hidden; }
  body {
    background: var(--canvas);
    font-family: "Arimo", Arial, sans-serif;
    display: flex;
    flex-direction: column;
    align-items: center;
    justify-content: center;
    gap: 44px;
  }
  .card {
    position: relative;
    width: 900px;
    height: 514px;
    background: var(--card);
    overflow: hidden;
    box-shadow: 0 6px 18px rgba(0,0,0,0.12);
  }
  .card-waves { position: absolute; inset: 0; width: 100%; height: 100%; }

  /* Back face */
  .brand-block {
    position: absolute;
    top: 86px;
    left: 0; right: 0;
    display: flex;
    flex-direction: column;
    align-items: center;
    gap: 18px;
  }
  .brand-dot {
    width: 64px; height: 64px;
    border-radius: 50%;
    background: var(--green);
  }
  .brand-name {
    font-weight: 700;
    color: var(--brown);
    font-size: 46px;
    letter-spacing: 3px;
    text-align: center;
    line-height: 1.1;
    text-transform: uppercase;
  }
  .website {
    position: absolute;
    top: 318px;
    left: 0; right: 0;
    text-align: center;
    color: var(--green);
    font-weight: 700;
    font-size: 24px;
    letter-spacing: 1px;
  }

  /* Front face */
  .person {
    position: absolute;
    top: 58px; left: 60px;
  }
  .person-name {
    color: var(--ink);
    font-weight: 700;
    font-size: 34px;
    letter-spacing: 1px;
    word-spacing: 6px;
  }
  .person-title {
    color: var(--olive);
    font-weight: 700;
    font-size: 22px;
    margin-top: 4px;
    letter-spacing: 1px;
  }
  .contacts {
    position: absolute;
    top: 218px; left: 60px;
    list-style: none;
    display: flex;
    flex-direction: column;
    gap: 14px;
  }
  .contacts li {
    display: flex;
    align-items: center;
    gap: 16px;
    color: var(--ink);
    font-size: 24px;
  }
  .contacts svg { width: 26px; height: 26px; flex: none; }
  .front-brand {
    position: absolute;
    top: 150px; right: 70px;
    display: flex;
    flex-direction: column;
    align-items: center;
    gap: 16px;
    width: 380px;
  }
  .front-brand .brand-name { font-size: 40px; }
</style>
</head>
<body>

  <section class="card card-back" aria-label="Business card back">
    <svg class="card-waves" viewBox="0 0 900 514" preserveAspectRatio="none" aria-hidden="true">
      <path d="M0 352 C 220 372, 520 388, 900 408 L 900 446 C 520 424, 220 404, 0 388 Z" fill="var(--green)"/>
      <path d="M0 420 C 240 430, 560 452, 900 470 L 900 492 C 560 478, 240 456, 0 446 Z" fill="var(--olive)"/>
    </svg>
    <div class="brand-block">
      <div class="brand-dot"></div>
      <div class="brand-name">Quill Ridge<br>Aviation</div>
    </div>
    <p class="website">WWW.QUILLRIDGE-AIR.COM</p>
  </section>

  <section class="card card-front" aria-label="Business card front">
    <svg class="card-waves" viewBox="0 0 900 514" preserveAspectRatio="none" aria-hidden="true">
      <path d="M0 372 C 200 368, 380 430, 620 420 C 760 414, 840 396, 900 392 L 900 430 C 840 434, 760 452, 620 458 C 380 466, 200 404, 0 404 Z" fill="var(--green)"/>
      <path d="M0 440 C 220 436, 420 480, 640 472 C 770 466, 850 450, 900 446 L 900 470 C 850 476, 770 494, 640 500 C 420 508, 220 468, 0 470 Z" fill="var(--olive)"/>
    </svg>

    <div class="person">
      <h1 class="person-name">Your Name Here</h1>
      <p class="person-title">Title Here</p>
    </div>

    <ul class="contacts">
      <li>
        <svg viewBox="0 0 24 24" aria-label="Phone"><path d="M6.6 10.8a15 15 0 0 0 6.6 6.6l2.2-2.2a1 1 0 0 1 1-.25 11.4 11.4 0 0 0 3.6.57 1 1 0 0 1 1 1V20a1 1 0 0 1-1 1A17 17 0 0 1 3 4a1 1 0 0 1 1-1h3.5a1 1 0 0 1 1 1c0 1.25.2 2.45.57 3.6a1 1 0 0 1-.25 1z" fill="var(--green-dark)"/></svg>
        <span>0815550192047</span>
      </li>
      <li>
        <svg viewBox="0 0 24 24" aria-label="Fax"><rect x="6" y="3" width="12" height="6" fill="none" stroke="var(--green-dark)" stroke-width="2"/><rect x="3" y="9" width="18" height="9" rx="1.5" fill="var(--green-dark)"/><rect x="7" y="14" width="10" height="7" fill="#fff" stroke="var(--green-dark)" stroke-width="2"/></svg>
        <span>0815550192047</span>
      </li>
      <li>
        <svg viewBox="0 0 24 24" aria-label="Email"><rect x="2" y="5" width="20" height="14" fill="var(--green-dark)"/><path d="M3 6l9 7 9-7" fill="none" stroke="#fff" stroke-width="1.8"/></svg>
        <span>mail@quillridge-air.com</span>
      </li>
    </ul>

    <div class="front-brand">
      <div class="brand-dot"></div>
      <div class="brand-name">Quill Ridge<br>Aviation</div>
    </div>
  </section>

</body>
</html>
```